Timeline flyer

Hi, we are an agency, our business is to orienteates student to study abroad in Germany. For that, we enroll them in language schools in Germany and help them to find an accomodation.
Students are always lost we thinked about a timeline to help them figure out what they have to do once in Germany so they don't miss delays.
You can find in the attachement an example that i made in powerpoint but it's really basic and it's only for u so you can understant what the timeline should look like.
We need two time lines.
For the first one (file first timeline)
Title : Procédure pour intégrer le semestre d’hiver dans les universités Allemandes
The first paragraph (up on the left in my proposition) : L’étudiant devra pendant ces mois débuter ses cours d’allemand en Tunisie et les poursuivre en Allemagne après l’obtention du Visa d’étude. L’atteinte du niveau C1 est primordiale pour la bonne réussite du test Kel ou le PLQ.
The second paragraph (below on the left in my proposition) : L’étudiant devra à cette date avoir déjà passer le test KEL ou le PLQ pour pouvoir être à temps pour les inscriptions universitaires. Il faut compter 6 semaines pour le test Kel et 2 à 3 semaines pour obtenir les résultats des tests.
The third one (up on the right in my proposition) : Le dernier délais d’inscription pour pouvoir intégrer une université Allemande pendant la rentrée hivernale (15 Octobre).
The last one (below on the right in my proposition) : Rentrée universitaire
For the second one (file second timeline) :
Title : Procédure pour intégrer le semestre d’été dans les universités Allemandes *
The third one (up on the right in my proposition) : Le dernier délais d’inscription pour pouvoir intégrer une université Allemande pendant la rentrée estivale (15 Avril).
There is also an additional sentence below in the right for this one : * Les spécialités assurées pendant les semestres d’été sont limitées.
You can also find in the attachement our flyers (so you can inspire youself with the color and the design), we want our student to recognize that the flyer is related to our agency so please try to use colors that are matched with the other flyer.
Also, you can find our Logo in the attachement.
Thank you :)
Waiting for your propositions ! :)

```html
<!DOCTYPE html>
<html lang="fr">
<head>
<meta charset="utf-8">
<title>Brivano centre – Timeline flyer</title>
<link href="https://fonts.googleapis.com/css2?family=Source+Sans+3:wght@400;600;700&family=Bebas+Neue&display=swap" rel="stylesheet">
<style>
  :root {
    --yellow: #dcdf00;
    --yellow-light: #eef04a;
    --yellow-deep: #b9bc00;
    --ink: #1f1f1f;
    --charcoal: #2b2b2b;
    --paper: #f1f1f1;
    --paper-shade: #dcdcdc;
    --backdrop: #e6e6e6;
    --text: #2a2a2a;
    --white: #ffffff;
  }
  * { margin: 0; padding: 0; box-sizing: border-box; }
  html, body { width: 1200px; height: 1200px; overflow: hidden; }
  body { background: var(--backdrop); font-family: "Source Sans 3", sans-serif; color: var(--text); }

  .flyer {
    position: absolute; left: 181px; top: 7px;
    width: 838px; height: 1185px; overflow: hidden;
    background: linear-gradient(160deg, var(--white) 0%, var(--paper) 45%, var(--paper-shade) 70%, var(--paper) 100%);
  }
  .decor { position: absolute; inset: 0; }

  .brand {
    position: absolute; left: 70px; top: 130px;
    display: flex; align-items: center; gap: 12px;
    font-family: "Source Sans 3", sans-serif; font-weight: 700;
    color: var(--white); font-size: 46px; line-height: 1;
  }
  .brand-dot { width: 18px; height: 18px; border-radius: 50%; background: var(--yellow); flex: none; }
  .brand-name { display: block; width: 190px; }

  .tab-title {
    position: absolute; text-align: center; font-weight: 700;
    color: var(--ink); line-height: 32px;
  }
  .tab-title.winter { left: 145px; top: 421px; width: 535px; font-size: 22px; }
  .tab-title.summer { left: 190px; top: 741px; width: 445px; font-size: 22px; }

  .para { position: absolute; text-align: justify; line-height: 1.35; }
  .para p + p { margin-top: 10px; }
  .winter-left { left: 62px; top: 505px; width: 353px; font-size: 14px; }
  .winter-right { left: 438px; top: 511px; width: 328px; font-size: 14px; }
  .summer-left { left: 70px; top: 830px; width: 334px; font-size: 15.5px; }
  .summer-right { left: 438px; top: 830px; width: 334px; font-size: 15.5px; }
  .summer-note { left: 438px; top: 987px; width: 334px; font-size: 15.5px; text-align: left; }

  .tag-label { position: absolute; font-weight: 600; color: var(--ink); }
  .tag-label.winter { left: 457px; top: 614px; font-size: 27px; }
  .tag-label.summer { left: 455px; top: 917px; font-size: 24px; font-weight: 700; }

  .site { position: absolute; left: 35px; top: 1134px; color: var(--white); font-weight: 700; font-size: 19px; letter-spacing: 1px; }
  .contact {
    position: absolute; left: 326px; top: 1104px; width: 500px; text-align: center;
    font-family: "Bebas Neue", sans-serif; font-size: 52px; color: var(--white);
    -webkit-text-stroke: 1.5px var(--ink); letter-spacing: 0.5px;
  }
</style>
</head>
<body>
  <main class="flyer">
    <svg class="decor" width="838" height="1185" viewBox="0 0 838 1185" aria-hidden="false">
      <defs>
        <linearGradient id="photoTone" x1="0" y1="0" x2="1" y2="1">
          <stop offset="0" stop-color="#e9eef2"/>
          <stop offset="0.5" stop-color="#d9c7b4"/>
          <stop offset="1" stop-color="#9aa3ad"/>
        </linearGradient>
        <linearGradient id="tabTone" x1="0" y1="0" x2="0" y2="1">
          <stop offset="0" stop-color="var(--yellow-light)"/>
          <stop offset="1" stop-color="var(--yellow)"/>
        </linearGradient>
      </defs>

      <polygon class="hero-photo" role="img" aria-label="Photo de groupe d'étudiants souriants levant le pouce dans une salle de cours" points="290,0 838,0 838,403 300,262" fill="url(#photoTone)"/>
      <polygon class="hero-band" points="300,262 838,403 838,460 410,318 400,322 316,295" fill="var(--yellow)"/>
      <polygon class="hero-band-shade" points="410,318 838,460 838,470 410,326" fill="var(--yellow-deep)"/>

      <circle class="badge-ring" cx="95" cy="148" r="240" fill="var(--yellow)"/>
      <circle class="badge-disc" cx="85" cy="135" r="230" fill="var(--charcoal)"/>

      <!-- winter section -->
      <polygon class="tab" points="172,418 652,418 680,486 145,486" fill="url(#tabTone)" stroke="var(--ink)" stroke-width="2"/>
      <rect class="frame" x="38" y="487" width="753" height="227" fill="none" stroke="var(--ink)" stroke-width="3"/>
      <polygon class="tag" points="437,607 738,607 758,636 738,665 437,665" fill="var(--yellow)" stroke="var(--ink)" stroke-width="3"/>

      <!-- summer section -->
      <polygon class="tab" points="215,739 612,739 635,806 190,806" fill="url(#tabTone)" stroke="var(--ink)" stroke-width="2"/>
      <path class="frame" d="M39,1096 V808 H791 V1073" fill="none" stroke="var(--ink)" stroke-width="3"/>
      <polygon class="tag" points="437,912 672,912 690,936 672,961 437,961" fill="var(--yellow)" stroke="var(--ink)" stroke-width="3"/>

      <!-- footer -->
      <rect class="footer-dark" x="0" y="1096" width="838" height="89" fill="var(--charcoal)"/>
      <polygon class="footer-yellow" points="261,1185 322,1073 838,1073 838,1185" fill="var(--yellow)"/>
      <line x1="322" y1="1073" x2="838" y2="1073" stroke="var(--ink)" stroke-width="3"/>
    </svg>

    <div class="brand"><span class="brand-dot"></span><span class="brand-name">Brivano centre</span></div>

    <h2 class="tab-title winter">Procédure pour intégrer le semestre d’hiver<br>dans les universités Allemandes</h2>
    <div class="para winter-left">
      <p>L’étudiant devra pendant ces mois débuter ses cours d’allemand en Tunisie et les poursuivre en Allemagne après l’obtention du Visa d’étude. L’atteinte du niveau C1 est primordiale pour la bonne réussite du test Kel ou le PLQ.</p>
      <p>L’étudiant devra à cette date avoir déjà passer le test KEL ou le PLQ pour pouvoir être à temps pour les inscriptions universitaires. Il faut compter 6 semaines pour le test Kel et 2 à 3 semaines pour obtenir les résultats des tests</p>
    </div>
    <div class="para winter-right">
      <p>Le dernier délais d’inscription pour pouvoir intégrer une université Allemande pendant la rentrée hivernale (15 Octobre).</p>
    </div>
    <span class="tag-label winter">Rentrée universitaire</span>

    <h2 class="tab-title summer">Procédure pour intégrer le semestre<br>d’été dans les universités Allemandes</h2>
    <div class="para summer-left">
      <p>L’étudiant devra pendant ces mois débuter ses cours d’allemand en Tunisie et les poursuivre en Allemagne après l’obtention du Visa d’étude. L’atteinte du niveau C1 est primordiale pour la bonne réussite du test Kel ou le PLQ.</p>
      <p>L’étudiant devra à cette date avoir déjà passer le test KEL ou le PLQ pour pouvoir être à temps pour les inscriptions universitaires. Il faut compter 6 semaines pour le test Kel et 2 à 3 semaines pour obtenir les résultats des tests.</p>
    </div>
    <div class="para summer-right">
      <p>Le dernier délais d’inscription pour pouvoir intégrer une université Allemande pendant la rentrée estivale (15 Avril).</p>
    </div>
    <span class="tag-label summer">Rentrée universitaire</span>
    <div class="para summer-note">
      <p>Les spécialités assurées pendant les semestres d’été sont limitées.</p>
    </div>

    <span class="site">www.brivano.org</span>
    <span class="contact">Contact us now: 71 555 204</span>
  </main>
</body>
</html>
```